Android Payment Application UI Design

We require a UI/UX design for an existing Android card-based payment application.

We're looking to improve the look + feel of the existing app. What we're after:
- Colour palette options
- Fonts
- Icons

See attached document for existing screen types, icons, etc.

All resources provided must be royalty free.

It's to run on a specialised device, with 720 x 1280 pixel resolution, in portrait only (landscape not required).

Please provide mockup examples of the new screen layout applied to the existing screens in the document.
Updates

Low designer entries

Target Market(s)

Retail business users

Font styles to use
Sans Serif

Colors

Designer to choose colors to be used in the design.

Requirements
Must have
• Looking for
• - modern design
• - simple colours, easy-to-read sans-serif fonts
• - cohesive, consistent design between screens

```html
<!DOCTYPE html>
<html lang="en">
<head>
<meta charset="utf-8">
<title>Veltra – Payment App Screens</title>
<link href="https://fonts.googleapis.com/css2?family=Lato:wght@300;400;700;900&display=swap" rel="stylesheet">
<style>
:root{
  --navy:#13009c;
  --blue:#0b5cf2;
  --ink:#111118;
  --muted:#8a8a96;
  --soft:#f7f8fc;
  --white:#ffffff;
  --line:#e6e8f0;
}
*{box-sizing:border-box;margin:0;padding:0}
html,body{width:1200px;height:750px;overflow:hidden;background:var(--white)}
body{position:relative;font-family:'Lato',sans-serif;color:var(--ink)}
.screen{position:absolute;overflow:hidden;background:var(--soft);box-shadow:0 6px 24px rgba(20,20,60,.08)}
.abs{position:absolute;line-height:1;white-space:nowrap}
.status{position:absolute;left:0;right:0;top:0;height:18px;font-size:9px;color:var(--white)}
.status.dark{color:var(--ink)}
.status .time{position:absolute;left:0;right:0;top:5px;text-align:center}
.status .sig{position:absolute;left:6px;top:5px;display:flex;gap:1px;align-items:flex-end}
.status .sig i{display:block;width:2px;background:currentColor}
.status .bat{position:absolute;right:6px;top:5px;display:flex;align-items:center;gap:3px}
.status .bat b{display:block;width:18px;height:7px;border:1px solid currentColor;border-radius:2px;background:currentColor}
.topbar{position:absolute;left:0;top:0;right:0;height:71px;background:var(--navy)}
.back{position:absolute;width:16px;height:12px}
.brand{position:absolute;top:41px;left:0;right:0;display:flex;justify-content:center;align-items:center;gap:6px;color:var(--white);font-weight:900;font-size:14px;letter-spacing:1px;line-height:1}
.brand .dot{width:12px;height:12px;border-radius:50%;background:var(--blue)}
.avatar{position:absolute;width:28px;height:28px;border-radius:50%;background:linear-gradient(135deg,#6a6a70,#2a2a30);border:2px solid var(--white)}
.h-title{font-weight:700;font-size:24px;color:var(--ink)}
.caption{font-size:10.5px;color:var(--muted)}
.label{font-size:8px;font-weight:700;letter-spacing:1.2px}
/* splash */
.splash{background:var(--navy)}
.splash .mark{position:absolute;left:112px;top:172px;width:60px;height:60px;border-radius:50%;background:var(--blue)}
.btn-login{position:absolute;left:54px;top:363px;width:177px;height:38px;border-radius:19px;background:var(--white);color:var(--navy);font-size:10.5px;font-weight:700;display:flex;align-items:center;justify-content:center}
/* home cards */
.tile{position:absolute;top:196px;width:137px;height:96px;background:var(--white);border-radius:4px;box-shadow:0 4px 14px rgba(20,20,60,.08)}
.tile svg{position:absolute;left:12px;top:14px}
.tile .t{position:absolute;left:12px;top:60px;font-size:14px;color:var(--navy);line-height:1}
.tile .d{position:absolute;left:12px;top:78px;font-size:10px;color:#a4a4ae;line-height:1;white-space:nowrap}
.pill{position:absolute;top:390px;height:26px;border-radius:13px;background:var(--blue);color:var(--white);font-size:10.5px;display:flex;align-items:center;justify-content:center;box-shadow:0 4px 10px rgba(11,92,242,.3);white-space:nowrap}
.act{font-size:8.5px;color:#2a2a34}
.act-day{font-size:6.5px;color:var(--muted)}
/* keypad */
.key{position:absolute;width:40px;text-align:center;font-size:18px;font-weight:300;color:#9a9aa4;line-height:1}
.band{position:absolute;left:0;right:0;height:51px;background:var(--blue);color:var(--white)}
</style>
</head>
<body>

<!-- Splash -->
<section class="screen splash" style="left:35px;top:28px;width:285px;height:506px">
  <div class="status"><div class="sig"><i style="height:3px"></i><i style="height:4px"></i><i style="height:5px"></i><i style="height:6px"></i></div><div class="time">9:41 AM</div><div class="bat">100% <b></b></div></div>
  <div class="mark"></div>
  <div class="abs" style="left:0;right:0;top:250px;text-align:center;color:var(--white);font-weight:700;font-size:18px">Veltra</div>
  <div class="abs" style="left:0;right:0;top:277px;text-align:center;color:var(--white);font-size:8.5px">your payment partner choice</div>
  <div class="btn-login">Log In</div>
  <div class="abs" style="left:0;right:0;top:413px;text-align:center;color:var(--white);font-size:10.5px;font-weight:700">Sign Up</div>
  <div class="abs" style="left:0;right:0;top:481px;text-align:center;color:var(--white);font-size:8.5px">Ver 0.0.1</div>
</section>

<!-- Sign in -->
<section class="screen" style="left:35px;top:558px;width:285px;height:220px;background:var(--white)">
  <div class="status dark"><div class="sig"><i style="height:3px"></i><i style="height:4px"></i><i style="height:5px"></i><i style="height:6px"></i></div><div class="time">9:41 AM</div><div class="bat">100% <b></b></div></div>
  <svg class="back" style="left:28px;top:45px" viewBox="0 0 16 12"><path d="M15 6H2M6 1L1 6l5 5" fill="none" stroke="#777" stroke-width="1.6"/></svg>
  <div class="abs h-title" style="left:28px;top:85px;font-size:29px">Sign In</div>
  <div class="abs caption" style="left:28px;top:124px">Sign in to continue</div>
</section>

<!-- Home -->
<section class="screen" style="left:350px;top:28px;width:298px;height:674px">
  <div class="topbar">
    <div class="status"><div class="sig"><i style="height:3px"></i><i style="height:4px"></i><i style="height:5px"></i><i style="height:6px"></i></div><div class="time">9:41 AM</div><div class="bat">100% <b></b></div></div>
    <svg class="back" style="left:28px;top:36px" viewBox="0 0 16 12"><path d="M15 6H2M6 1L1 6l5 5" fill="none" stroke="#fff" stroke-width="1.8"/></svg>
    <div class="brand" style="top:34px"><span class="dot"></span>VELTRA</div>
    <div class="avatar" role="img" aria-label="User profile photo" style="left:244px;top:30px"></div>
  </div>
  <div class="abs h-title" style="left:28px;top:104px;line-height:1.12">Hello there,<br>Nadia!</div>
  <div class="abs caption" style="left:28px;top:162px">How can we help you?</div>
  <div class="tile" style="left:28px">
    <svg width="26" height="18" viewBox="0 0 26 18"><rect x="1" y="1" width="24" height="16" rx="2" fill="none" stroke="var(--navy)" stroke-width="1.5"/><path d="M1 6h24M4 12h8" stroke="var(--navy)" stroke-width="1.5"/><circle cx="20" cy="12" r="1.5" fill="none" stroke="var(--navy)"/></svg>
    <div class="t">Sale</div><div class="d">Check your sales</div>
  </div>
  <div class="tile" style="left:178px">
    <svg width="22" height="22" viewBox="0 0 22 22"><path d="M4 9a7 7 0 0 1 13-3M18 13a7 7 0 0 1-13 3" fill="none" stroke="var(--navy)" stroke-width="1.6"/><path d="M17 2v4h-4M5 20v-4h4" fill="none" stroke="var(--navy)" stroke-width="1.6"/></svg>
    <div class="t">Reversal</div><div class="d">Put small description</div>
  </div>
  <div class="abs" style="left:28px;top:340px;font-size:17px;color:var(--navy)">Admin</div>
  <div class="abs caption" style="left:28px;top:362px">Short description about admin menu</div>
  <div class="pill" style="left:27px;width:76px">Payment</div>
  <div class="pill" style="left:118px;width:126px">Connect An Account</div>
  <div class="pill" style="left:258px;width:90px;justify-content:flex-start;padding-left:13px">Manage</div>
  <div class="abs" style="left:28px;top:450px;font-size:17px;color:var(--navy)">Recent Activity</div>
  <div class="abs caption" style="left:28px;top:472px">Small description for Activity</div>
  <div class="abs label" style="left:28px;top:502px;font-size:7.5px;color:var(--ink)">YESTERDAY</div>
  <div class="abs act-day" style="left:28px;top:527px">1:24PM</div>
  <div class="abs act" style="left:80px;top:526px">You have succesfully connected your account</div>
  <div class="abs label" style="left:28px;top:559px;font-size:7.5px;color:var(--ink)">LAST WEEK</div>
  <div class="abs act-day" style="left:28px;top:584px">FRI</div>
  <div class="abs act" style="left:81px;top:583px">Purchased an Tablet Z</div>
  <div class="abs act-day" style="left:28px;top:605px">TUE</div>
  <div class="abs act" style="left:81px;top:604px">Edit Password and details</div>
  <div class="abs label" style="left:28px;top:637px;color:var(--blue)">VIEW MORE ACTIVITY</div>
</section>

<!-- Amount entry -->
<section class="screen" style="left:682px;top:25px;width:299px;height:531px;background:var(--white)">
  <div class="topbar" style="height:230px">
    <div class="status"><div class="sig"><i style="height:3px"></i><i style="height:4px"></i><i style="height:5px"></i><i style="height:6px"></i></div><div class="time">9:41 AM</div><div class="bat">100% <b></b></div></div>
    <svg class="back" style="left:28px;top:36px" viewBox="0 0 16 12"><path d="M15 6H2M6 1L1 6l5 5" fill="none" stroke="#fff" stroke-width="1.8"/></svg>
    <div class="brand" style="top:37px"><span class="dot"></span>VELTRA</div>
    <div class="avatar" role="img" aria-label="User profile photo" style="left:244px;top:33px"></div>
    <div class="abs" style="left:29px;top:100px;font-size:22px;font-weight:700;color:var(--white)">Amount Entry</div>
    <div class="abs" style="left:29px;top:130px;font-size:10.5px;color:var(--white)">Check your sale</div>
    <div class="abs label" style="left:29px;top:174px;font-size:7px;color:var(--blue);font-weight:400">ENTER AMOUNT</div>
    <div class="abs" style="left:28px;top:188px;font-size:32px;font-weight:300;color:var(--blue)">09.56</div>
  </div>
  <div class="band" style="top:230px;display:flex;align-items:center;justify-content:center;font-size:9px;font-weight:700;letter-spacing:1px">PROCEED</div>
  <div class="key" style="left:41px;top:315px">1</div><div class="key" style="left:130px;top:315px">2</div><div class="key" style="left:218px;top:315px">3</div>
  <div class="key" style="left:41px;top:369px">4</div><div class="key" style="left:130px;top:369px">5</div><div class="key" style="left:218px;top:369px">6</div>
  <div class="key" style="left:41px;top:423px">7</div><div class="key" style="left:130px;top:423px">8</div><div class="key" style="left:218px;top:423px">9</div>
  <div class="abs" style="left:58px;top:486px;width:6px;height:6px;border-radius:50%;background:#b4b4bc"></div>
  <div class="key" style="left:130px;top:480px">0</div>
  <svg class="abs" style="left:228px;top:482px" width="18" height="12" viewBox="0 0 18 12"><path d="M5 0h13v12H5L0 6z" fill="#c4c4cc"/><path d="M9 3l6 6M15 3l-6 6" stroke="#fff" stroke-width="1.4"/></svg>
</section>

<!-- Enter pin -->
<section class="screen" style="left:682px;top:624px;width:305px;height:160px">
  <div class="topbar" style="height:72px">
    <div class="status"><div class="sig"><i style="height:3px"></i><i style="height:4px"></i><i style="height:5px"></i><i style="height:6px"></i></div><div class="time">9:41 AM</div><div class="bat">100% <b></b></div></div>
    <svg class="back" style="left:28px;top:38px" viewBox="0 0 16 12"><path d="M15 6H2M6 1L1 6l5 5" fill="none" stroke="#fff" stroke-width="1.8"/></svg>
    <div class="brand" style="top:38px"><span class="dot"></span>VELTRA</div>
    <div class="avatar" role="img" aria-label="User profile photo" style="left:249px;top:33px"></div>
  </div>
  <div class="abs h-title" style="left:29px;top:106px;font-size:22px">Enter Pin</div>
</section>

<!-- Enter manually -->
<section class="screen" style="left:1016px;top:28px;width:300px;height:533px">
  <div class="topbar">
    <div class="status"><div class="sig"><i style="height:3px"></i><i style="height:4px"></i><i style="height:5px"></i><i style="height:6px"></i></div><div class="time" style="text-align:left;left:132px">9:41 AM</div></div>
    <svg class="back" style="left:28px;top:36px" viewBox="0 0 16 12"><path d="M15 6H2M6 1L1 6l5 5" fill="none" stroke="#fff" stroke-width="1.8"/></svg>
    <div class="brand" style="top:37px;left:112px;right:auto"><span class="dot"></span>VELTRA</div>
  </div>
  <div class="abs h-title" style="left:29px;top:103px;font-size:23px">Enter Manually</div>
  <div class="abs caption" style="left:29px;top:134px">Please enter your Card Number</div>
  <div class="abs label" style="left:29px;top:248px;font-size:7px;color:var(--muted);font-weight:400">CARD NUMBER</div>
  <div class="abs" style="left:29px;top:273px;font-size:10.5px;color:#b4b4bc">0000 - 0000 - 0000 - 0000</div>
  <div class="abs label" style="left:88px;top:311px;color:var(--blue)">ENTER YOUR CARD NUMBER</div>
  <div class="band" style="top:481px">
    <div class="abs" style="left:30px;top:18px;font-size:8px">£</div>
    <div class="abs" style="left:38px;top:13px;font-size:24px;font-weight:300">09.56</div>
  </div>
</section>

</body>
</html>
```